Verlune Magician

I want the business card for my business to give to people who watch that later I will be employed to show magic here is my website http://www.verlunemagicien-exemple.fr/I want the interesting design , i am very opened for formal and informal, I watch a lot of design so don't stick to the common shape and form but i hope it can also be produced the thing to write on will be the same as in picture that i will upload , i also will upload the logo for you that so can be easy to useDenis CostilleMagicianMAGICIAN VERLUNE 17 rue des Tilleuls - 71490 VERCLAIRE contact@verlunemagicien-exemple.fr tel. 0399 476 093 tel. 0664 219 570

```html
<!DOCTYPE html>
<html lang="fr">
<head>
<meta charset="utf-8">
<title>Verlune Magicien – cartes de visite</title>
<link rel="stylesheet" href="https://fonts.googleapis.com/css2?family=Jost:wght@400;500;600&display=swap">
<style>
  :root {
    --backdrop: #1e1e1e;
    --card: #ffffff;
    --ink: #111111;
    --ink-soft: #2a2a2a;
    --rule: #333333;
    --portrait-dark: #141414;
    --portrait-light: #3a3a3a;
  }
  * { box-sizing: border-box; margin: 0; padding: 0; }
  html, body {
    width: 1200px; height: 895px; overflow: hidden;
    background: var(--backdrop);
    font-family: "Jost", sans-serif;
    color: var(--ink);
  }
  .stage { position: relative; width: 1200px; height: 895px; }
  .card {
    position: absolute; left: 250px;
    width: 700px; height: 400px;
    background: var(--card);
    box-shadow: 0 10px 30px rgba(0,0,0,.6);
  }
  .card--front { top: 32px; }
  .card--back { top: 463px; }

  .portrait {
    position: absolute;
    background: linear-gradient(160deg, var(--portrait-light), var(--portrait-dark));
    border-radius: 46% 46% 14% 14% / 30% 30% 10% 10%;
  }
  .card--front .portrait { left: 95px; top: 60px; width: 250px; height: 280px; }
  .card--back .portrait { left: 95px; top: 120px; width: 170px; height: 165px; }

  .brand {
    position: absolute;
    font-weight: 400;
    letter-spacing: 2px;
    color: var(--ink);
    display: flex; align-items: center; gap: 10px;
  }
  .brand__mark { width: 10px; height: 10px; background: var(--ink); }
  .card--front .brand { left: 405px; top: 190px; font-size: 44px; }
  .card--back .brand { left: 95px; top: 292px; font-size: 30px; }
  .card--back .brand .brand__mark { width: 7px; height: 7px; }

  .details { position: absolute; left: 330px; top: 88px; }
  .block {
    border-left: 2px solid var(--rule);
    padding-left: 20px;
    margin-bottom: 18px;
  }
  .person__name { font-size: 28px; font-weight: 600; letter-spacing: .5px; line-height: 1; }
  .person__role { font-size: 14px; letter-spacing: 1px; margin-top: 4px; }
  .address { font-size: 15px; line-height: 1.35; color: var(--ink-soft); letter-spacing: .3px; }
  .contact { list-style: none; font-size: 16px; line-height: 1.45; color: var(--ink-soft); }
  .contact li { display: flex; align-items: center; gap: 10px; }
  .contact svg { width: 12px; height: 12px; fill: var(--ink); flex: none; }
</style>
</head>
<body>
<main class="stage">

  <section class="card card--front">
    <div class="portrait" role="img" aria-label="Illustration en noir et blanc du magicien tenant une carte à jouer"></div>
    <div class="brand"><span class="brand__mark"></span>VERLUNE</div>
  </section>

  <section class="card card--back">
    <div class="portrait" role="img" aria-label="Illustration en noir et blanc du magicien tenant une carte à jouer"></div>
    <div class="brand"><span class="brand__mark"></span>VERLUNE</div>

    <div class="details">
      <div class="block person">
        <p class="person__name">LUCIEN MARBEC</p>
        <p class="person__role">MAGICIEN</p>
      </div>
      <div class="block address">
        <p>VERLUNE MAGICIEN</p>
        <p>17 rue des Tilleuls - 71490 VERCLAIRE</p>
      </div>
      <ul class="block contact">
        <li><svg viewBox="0 0 12 12"><path d="M2.5 0.5l2 2.5-1.2 1.3c.7 1.6 2 2.9 3.6 3.6L8.2 6.7l2.6 2-1 2.6C5 11 1 7 .7 2.3z"/></svg>0399 476 093</li>
        <li><svg viewBox="0 0 12 12"><path d="M2.5 0.5l2 2.5-1.2 1.3c.7 1.6 2 2.9 3.6 3.6L8.2 6.7l2.6 2-1 2.6C5 11 1 7 .7 2.3z"/></svg>0664 219 570</li>
        <li><svg viewBox="0 0 12 12"><path d="M0 2h12v8H0z M0 2l6 4.5L12 2" stroke="#fff" stroke-width=".8"/></svg>contact@verlunemagicien-exemple.fr</li>
        <li><svg viewBox="0 0 12 12"><circle cx="6" cy="6" r="5.5"/><path d="M.5 6h11M6 .5v11M2 3h8M2 9h8" stroke="#fff" stroke-width=".7" fill="none"/></svg>www.verlunemagicien-exemple.fr</li>
      </ul>
    </div>
  </section>

</main>
</body>
</html>
```